Psychiatric Office Needs a Website- 1st Time Ever!

Been in practice since 2003 with no website, but finally ready to dive in. We are Maplecrest Behavioral Healthcare, a mental health outpatient practice based in Fayetteville, Georgia that sees diverse individuals and families from childhood to advanced age for a variety of conditions. We've grown by word of mouth and referral but would now like to have a digital footprint. Be the pioneer of our website and we will be sure to share. We would like to see designs that are modern, animated, fairly colorful, easy to read, and caters to all ages. Also, we would like the design to take the whole page (not be centered) and can be viewed well on phone/tablet. Please see our outline for more information. Our motto/slogan is: Maplecrest Behavioral Healthcare- A step forward in your wellness journey, so the design should try to reflect that.
Updates

Target Market(s)

Children through elderly

Industry/Entity Type

Medical

Logo Text

Stepping forward in your wellness journey

Number of Pages Required

1 page

Colors

Designer to choose colors to be used in the design.

Requirements
Must have
• Animation or moving pictures.
• Color.
• Concise.
• User friendly
• Diversity in the stock photos

```html
<!DOCTYPE html>
<html lang="en">
<head>
<meta charset="utf-8">
<title>Maplecrest Behavioral Healthcare</title>
<link href="https://fonts.googleapis.com/css2?family=Lato:wght@400;700;900&display=swap" rel="stylesheet">
<style>
:root{
  --teal:#1aaabf;
  --blue:#1f74b8;
  --navy:#11507f;
  --green:#6cae2f;
  --ink:#333a40;
  --muted:#7b8288;
  --light:#f1f1f1;
  --footer:#5b5b5b;
  --footer-dark:#474747;
  --white:#ffffff;
}
*{box-sizing:border-box;margin:0;padding:0}
html,body{width:1200px;height:2679px;overflow:hidden}
body{position:relative;font-family:'Lato',sans-serif;color:var(--ink);background:var(--white)}
.abs{position:absolute}
.topbar{left:0;top:0;width:1200px;height:34px;background:var(--teal)}
.topbar .links{left:161px;top:9px;display:flex;gap:22px;font-size:11px;font-weight:700;color:var(--white)}
.topbar .social{right:161px;top:11px;display:flex;gap:12px}
.topbar .social span{width:11px;height:11px;border-radius:50%;background:var(--white)}
.nav{left:0;top:34px;width:1200px;height:77px;background:var(--white)}
.brand{left:161px;top:20px;display:flex;align-items:center;gap:9px}
.brand .mark{width:34px;height:34px;border-radius:50%;background:var(--teal)}
.brand .name{width:150px;font-size:14px;font-weight:700;line-height:1.15;color:var(--green)}
.menu{left:409px;top:33px;display:flex;gap:26px;font-size:11.5px;font-weight:700;letter-spacing:.4px;color:var(--ink)}
.menu .active{position:relative}
.menu .active::after{content:"";position:absolute;left:-4px;right:-4px;top:34px;height:3px;background:var(--green)}
.search{left:1023px;top:31px}
.hero{left:0;top:111px;width:1200px;height:407px;background:linear-gradient(100deg,#4d4f55 0%,#8d8f94 40%,#b7b4b0 70%,#6f6e6d 100%)}
.hero-text{left:0;top:135px;width:1200px;text-align:center;color:var(--white)}
.hero-text h1{font-size:31px;font-weight:700}
.hero-text p{font-size:33px;font-weight:400;line-height:1.22;margin-top:4px}
.btn-green{left:506px;top:419px;width:188px;height:40px;border-radius:6px;background:var(--green);color:var(--white);font-size:14px;font-weight:700;text-align:center;line-height:40px}
.arrow{top:273px;width:66px;height:52px;background:rgba(40,40,40,.45);display:flex;align-items:center;justify-content:center}
.info{left:0;top:518px;width:1200px;height:84px;background:var(--light)}
.info .item{top:20px;display:flex;align-items:center;gap:8px;font-size:10px;line-height:1.6;color:var(--ink)}
.ico{width:38px;height:38px;border-radius:50%;background:var(--teal);display:flex;align-items:center;justify-content:center;flex:none}
.sec-title{font-size:29px;font-weight:700;color:var(--ink)}
.rule{width:56px;height:3px;background:var(--teal)}
.about-title{left:161px;top:658px}
.about-rule{left:161px;top:706px}
.about-text{left:161px;top:730px;width:420px;font-size:13.5px;line-height:1.8;color:var(--ink)}
.btn-teal{left:161px;top:831px;width:100px;height:40px;border-radius:6px;background:var(--teal);color:var(--white);font-size:13px;font-weight:700;text-align:center;line-height:40px}
.about-photo{left:611px;top:634px;width:427px;height:270px;background:linear-gradient(120deg,#d8d8d6,#a8a29b 55%,#e6e4e1)}
.vision{left:161px;top:932px;width:877px;height:300px;background:var(--blue);color:var(--white)}
.vision h2{position:absolute;left:0;top:16px;width:100%;text-align:center;font-size:29px;font-weight:700}
.vbox{top:72px;width:340px;height:203px;border:1px solid var(--white);text-align:center;font-size:13px;font-weight:700;line-height:1.95;padding:20px 26px 0}
.vbox .btn{position:absolute;left:50%;bottom:18px;transform:translateX(-50%);width:84px;height:34px;border-radius:5px;background:var(--navy);font-size:11.5px;line-height:34px}
.svc-title{left:0;top:1255px;width:1200px;text-align:center}
.svc-rule{left:572px;top:1303px}
.svc{width:202px;height:182px;text-align:center;padding-top:30px}
.svc h3{font-size:18px;font-weight:400;line-height:1.3;color:var(--ink)}
.svc .bar{width:56px;height:3px;background:var(--green);margin:10px auto 14px}
.svc p{font-size:12px;line-height:1.8;color:var(--muted)}
.svc.on{background:var(--blue)}
.svc.on h3,.svc.on p{color:var(--white);font-weight:700}
.svc.on h3{font-weight:400}
.svc.on .bar{background:var(--white)}
.conditions{left:161px;top:1756px;width:877px;height:298px;background:linear-gradient(90deg,#6f9fcf,#8cb6dc 50%,#7ea9d3);color:var(--white)}
.conditions h2{position:absolute;left:0;top:14px;width:100%;text-align:center;font-size:30px;font-weight:700;letter-spacing:2px}
.cond-list{top:88px;display:flex;flex-direction:column;gap:18px;font-size:14.5px;font-weight:700}
.cond-list div{display:flex;align-items:center;gap:12px}
.tick{width:27px;height:27px;background:var(--white);border-radius:3px;display:flex;align-items:center;justify-content:center;flex:none}
.btn-white{left:392px;top:244px;width:94px;height:36px;border-radius:6px;background:var(--white);color:var(--blue);font-size:13px;font-weight:700;text-align:center;line-height:36px}
.contact{left:0;top:2086px;width:600px;height:300px;background:var(--light)}
.contact h3,.appt h3{font-size:22px;font-weight:400}
.appt{left:600px;top:2086px;width:600px;height:300px;background:var(--blue);color:var(--white)}
.field{font-size:10px;font-weight:700;padding-bottom:6px;border-bottom:1px solid var(--teal);width:136px;display:flex;justify-content:space-between}
.send{left:74px;top:249px;width:62px;height:26px;border-radius:4px;background:var(--navy);font-size:10px;font-weight:700;text-align:center;line-height:26px}
.footer{left:0;top:2386px;width:1200px;height:239px;background:var(--footer);color:var(--white)}
.footer h4{font-size:18px;font-weight:700}
.footer .rule{margin-top:10px}
.flist div{font-size:11px;font-weight:700;padding:8px 0;border-bottom:1px dotted var(--teal);width:200px}
.copy{left:0;top:2625px;width:1200px;height:54px;background:var(--footer-dark);color:var(--white);font-size:12px;font-weight:700;text-align:center;line-height:54px}
</style>
</head>
<body>

<div class="abs topbar">
  <div class="abs links"><span>Contact us</span><span>About us</span><span>Faqs</span><span>Online payment</span><span>Our providers</span></div>
  <div class="abs social"><span></span><span></span><span></span><span></span></div>
</div>

<header class="abs nav">
  <div class="abs brand"><span class="mark"></span><span class="name">Maplecrest Behavioral Healthcare</span></div>
  <nav class="abs menu">
    <span class="active">Home</span><span>About Us</span><span>Services</span><span>Conditions We Treat</span><span>New Patients</span><span>Prescription Refills</span>
  </nav>
  <svg class="abs search" width="14" height="14" viewBox="0 0 14 14"><circle cx="6" cy="6" r="4.5" fill="none" stroke="#1aaabf" stroke-width="2"/><line x1="9.3" y1="9.3" x2="13" y2="13" stroke="#1aaabf" stroke-width="2"/></svg>
</header>

<section class="abs hero" role="img" aria-label="Photo of a smiling older couple talking with a counselor"></section>
<div class="abs hero-text">
  <h1>Maplecrest Behavioral Healthcare</h1>
  <p>A step forward in your<br>wellness journey</p>
</div>
<div class="abs btn-green">Make an appointment</div>
<div class="abs arrow" style="left:0"><svg width="14" height="22" viewBox="0 0 14 22"><polyline points="11,2 3,11 11,20" fill="none" stroke="#fff" stroke-width="2"/></svg></div>
<div class="abs arrow" style="right:0"><svg width="14" height="22" viewBox="0 0 14 22"><polyline points="3,2 11,11 3,20" fill="none" stroke="#fff" stroke-width="2"/></svg></div>

<section class="abs info">
  <div class="abs item" style="left:341px"><span class="ico"><svg width="12" height="20" viewBox="0 0 12 20"><rect x="1" y="1" width="10" height="18" rx="2" fill="none" stroke="#fff" stroke-width="2"/><circle cx="6" cy="15" r="1.2" fill="#fff"/></svg></span><span><b>Phone:</b> (770) 555-0148<br><b>Fax:</b> (678) 555-0193</span></div>
  <div class="abs item" style="left:526px"><span class="ico"><svg width="14" height="20" viewBox="0 0 14 20"><path d="M7 19C2 12 1 9 1 7a6 6 0 0 1 12 0c0 2-1 5-6 12z" fill="#fff"/><circle cx="7" cy="7" r="2.3" fill="#1aaabf"/></svg></span><span><b>Birchwood Ave W Ste 210</b><br>Fayetteville, GA 30215</span></div>
  <div class="abs item" style="left:728px"><span class="ico"><svg width="18" height="18" viewBox="0 0 18 18"><rect x="1" y="3" width="16" height="14" rx="1" fill="none" stroke="#fff" stroke-width="2"/><line x1="1" y1="7" x2="17" y2="7" stroke="#fff" stroke-width="2"/><line x1="5" y1="1" x2="5" y2="4" stroke="#fff" stroke-width="2"/><line x1="13" y1="1" x2="13" y2="4" stroke="#fff" stroke-width="2"/></svg></span><span><b>8:00am-5:00pm</b><br>Monday-Friday</span></div>
</section>

<h2 class="abs sec-title about-title">About Us</h2>
<div class="abs rule about-rule"></div>
<p class="abs about-text">Lorem ipsum dolor sit amet, consectetur adipiscing elit Aliquam at ligula risus. Sed porta purus lacus, nec condimentum dolor maximus in. Integer id mi sed purus porta pulvinar</p>
<div class="abs btn-teal">See More</div>
<div class="abs about-photo" role="img" aria-label="Photo of a patient in a counseling session with a therapist"></div>

<section class="abs vision">
  <h2>Vision &amp; Mission</h2>
  <div class="abs vbox" style="left:59px">To be the leading provider of outpatient psychiatric care in Atlanta Metro South, working together to promote (the) mental wellness of our community<span class="btn">See More</span></div>
  <div class="abs vbox" style="left:477px;padding-top:12px">To provide mental health services to children, adults, and the developmentally disabled population that is culturally sensitive regardless of age, race, gender, orientation, religion, or creed<span class="btn">See More</span></div>
</section>

<h2 class="abs sec-title svc-title">Our Services</h2>
<div class="abs rule svc-rule"></div>
<div class="abs svc" style="left:163px;top:1336px"><h3>Diagnostic evaluation<br>and treatment</h3><div class="bar"></div><p>Lorem ipsum dolor sit amet<br>consectetur adipiscing</p></div>
<div class="abs svc on" style="left:387px;top:1336px"><h3>Psychopharma<br>cology</h3><div class="bar"></div><p>Lorem ipsum dolor sit amet<br>consectetur adipiscing</p></div>
<div class="abs svc" style="left:613px;top:1336px"><h3>Bariatric pre-surgical<br>consultation</h3><div class="bar"></div><p>Lorem ipsum dolor sit amet<br>consectetur adipiscing</p></div>
<div class="abs svc" style="left:838px;top:1336px"><h3>Disability and<br>work-related reports</h3><div class="bar"></div><p>Lorem ipsum dolor sit amet<br>consectetur adipiscing</p></div>
<div class="abs svc" style="left:274px;top:1546px"><h3>Early childhood<br>Assessments</h3><div class="bar"></div><p>Lorem ipsum dolor sit amet<br>consectetur adipiscing</p></div>
<div class="abs svc" style="left:497px;top:1546px"><h3>Substance abuse<br>assessments</h3><div class="bar"></div><p>Lorem ipsum dolor sit amet<br>consectetur adipiscing</p></div>
<div class="abs svc" style="left:724px;top:1546px"><h3>Developmental<br>disabilities</h3><div class="bar"></div><p>Lorem ipsum dolor sit amet<br>consectetur adipiscing</p></div>

<section class="abs conditions" role="img" aria-label="Soft blue photo backdrop of a counseling conversation">
  <h2>Conditions We Treat</h2>
  <div class="abs cond-list" style="left:92px">
    <div><span class="tick"><svg width="16" height="14" viewBox="0 0 16 14"><polyline points="2,7 6,11 14,2" fill="none" stroke="#e2c60f" stroke-width="3"/></svg></span>Mood Disorders: Depression, Bipolar</div>
    <div><span class="tick"><svg width="16" height="14" viewBox="0 0 16 14"><polyline points="2,7 6,11 14,2" fill="none" stroke="#e2c60f" stroke-width="3"/></svg></span>Anxiety Disorders: Generalized Anxiety..</div>
    <div><span class="tick"><svg width="16" height="14" viewBox="0 0 16 14"><polyline points="2,7 6,11 14,2" fill="none" stroke="#e2c60f" stroke-width="3"/></svg></span>Common Disorders of Childhood: ADHD..</div>
  </div>
  <div class="abs cond-list" style="left:457px">
    <div><span class="tick"><svg width="16" height="14" viewBox="0 0 16 14"><polyline points="2,7 6,11 14,2" fill="none" stroke="#e2c60f" stroke-width="3"/></svg></span>Sleep Issues</div>
    <div><span class="tick"><svg width="16" height="14" viewBox="0 0 16 14"><polyline points="2,7 6,11 14,2" fill="none" stroke="#e2c60f" stroke-width="3"/></svg></span>Psychotic Disorders: Schizophrenia</div>
    <div><span class="tick"><svg width="16" height="14" viewBox="0 0 16 14"><polyline points="2,7 6,11 14,2" fill="none" stroke="#e2c60f" stroke-width="3"/></svg></span>And More: Addiction, Eating Disorders</div>
  </div>
  <div class="abs btn-white">See More</div>
</section>

<section class="abs contact">
  <h3 class="abs" style="left:236px;top:20px">Contact Info</h3>
  <div class="abs rule" style="left:236px;top:56px;height:2px"></div>
  <p class="abs" style="left:236px;top:76px;font-size:13px;font-weight:700">Need to discuss before treatment?</p>
  <div class="abs" style="left:236px;top:112px;display:flex;gap:8px;align-items:center;font-size:10px;line-height:1.7"><span class="ico" style="width:34px;height:34px"><svg width="11" height="18" viewBox="0 0 12 20"><rect x="1" y="1" width="10" height="18" rx="2" fill="none" stroke="#fff" stroke-width="2"/></svg></span><span><b>Phone:</b> (770) 555-0148<br><b>Fax:</b> (678) 555-0193</span></div>
  <div class="abs" style="left:236px;top:162px;display:flex;gap:8px;align-items:center;font-size:10px;line-height:1.7"><span class="ico" style="width:34px;height:34px"><svg width="13" height="18" viewBox="0 0 14 20"><path d="M7 19C2 12 1 9 1 7a6 6 0 0 1 12 0c0 2-1 5-6 12z" fill="#fff"/></svg></span><span><b>Birchwood Ave W Ste 210</b><br>Fayetteville, GA 30215</span></div>
  <p class="abs" style="left:236px;top:246px;width:210px;font-size:10px;line-height:1.6">The best contact you will get here lorem ipsum dolor sit amet.</p>
</section>

<section class="abs appt">
  <h3 class="abs" style="left:74px;top:20px">Fix An Appointment</h3>
  <div class="abs rule" style="left:74px;top:56px;height:2px"></div>
  <div class="abs field" style="left:74px;top:93px">Your Name</div>
  <div class="abs field" style="left:233px;top:93px">Email</div>
  <div class="abs field" style="left:74px;top:134px">Phone</div>
  <div class="abs field" style="left:233px;top:134px">Date<span>&#9662;</span></div>
  <div class="abs field" style="left:74px;top:175px;height:50px">Message</div>
  <div class="abs field" style="left:233px;top:175px">Service<span>&#9662;</span></div>
  <div class="abs send">Send</div>
</section>

<footer class="abs footer">
  <div class="abs" style="left:231px;top:22px"><h4>About us</h4><div class="rule"></div>
    <div style="display:flex;align-items:center;gap:7px;margin-top:18px"><span style="width:30px;height:30px;border-radius:50%;background:var(--teal)"></span><span style="font-size:12.5px;font-weight:700;color:var(--green);width:140px;line-height:1.15">Maplecrest Behavioral Healthcare</span></div>
    <p style="font-size:11px;font-weight:700;line-height:1.9;width:185px;margin-top:8px">Lorem ipsum. Proin gravida nibh vel velit auctor nibh id eliduis sed odio.</p></div>
  <div class="abs flist" style="left:476px;top:22px"><h4>Our Services</h4><div class="rule" style="border:0;padding:0;width:56px"></div>
    <div style="margin-top:10px">- Early childhood Assessments</div><div>- Psychopharmacology</div><div>- Diagnostic evaluation</div><div style="border:0">- Bariatric pre-surgical consultation</div></div>
  <div class="abs" style="left:770px;top:22px;font-size:11px;font-weight:700"><h4>Our Time Schedule</h4><div class="rule"></div>
    <p style="margin-top:18px">- Monday - Thursday</p><p style="margin-top:18px">8:00 Am - 5:00 Pm</p>
    <div style="width:200px;border-bottom:1px dotted var(--teal);margin-top:12px"></div>
    <p style="margin-top:24px">- Friday</p><p style="margin-top:18px">8:00 Am - 1:00 Pm</p></div>
</footer>
<div class="abs copy">Maplecrest Behavioral Healthcare &copy; 2017. All Rights Reserved</div>

</body>
</html>
```